Etiketten-Design für Kräuterbonbon-Metalldose
Marlene Vosk hat sehr viel Talent. Das Design ist absolut kreativ.
Zielgruppe
Unsere Firma VelbraCor verkauft verschiedene Sorten Kräuterbonbons.
Wir brauchen ein Etikett, dass auf eine Metall-Dose (Durchmesser 10 cam, Höhe ca. 3 cm) geklebt wird.
Zielgruppe: jung-alt
Aufgabenstellung
Der Name unserer Kräuterbonbons ist Pfeffling.
Wir möchten, dass unsere Kunden, wenn sie das Etikett sehen einen Bezug zur Schweiz herstellen können.
Wir verwenden für unsere Bonbons unterschiedliche Kräuter für verschiedene Anwendungen:
Konkret sind erstmal 4 Dosen geplant:
-Kräutermischung aus 16 Kräuter gegen Husten
-Salbei gegen Halsschmerzen
-Anis gegen Magenschmerzen
-Zitrone/Ingwer für die Nerven
Vorderseite: Produktbeschreibung
Rückseite: unsere Herstellerangaben
Größenangaben der Dose: Durchmesser 10 cm, Höhe ca. 3 cm
Im Anhang habe ich Ihnen noch weitere/ genauere Informationen zur Verfügung bereitgestellt!

```html
<!DOCTYPE html>
<html lang="de">
<head>
<meta charset="utf-8">
<title>Pfeffling – Etikett Kräutermischung</title>
<link rel="stylesheet" href="https://fonts.googleapis.com/css2?family=Fira+Sans:wght@400;700&display=swap">
<style>
  :root {
    --paper: #ffffff;
    --swiss-red: #d42a27;
    --swiss-red-deep: #b81f1f;
    --herb-green: #1f8a3b;
    --label-white: #ececec;
    --stripe-white: #f4f4f4;
    --sky: #b9d6dc;
    --meadow: #5fae48;
    --text-light: #ffffff;
  }
  html, body {
    margin: 0;
    padding: 0;
    width: 1200px;
    height: 849px;
    overflow: hidden;
    background: var(--paper);
  }
  .sheet {
    position: relative;
    width: 1200px;
    height: 849px;
  }
  .label {
    position: absolute;
    width: 360px;
    height: 360px;
    top: 244px;
  }
  .label--scenic { left: 163px; }
  .label--plain { left: 680px; }
  .label svg { display: block; width: 100%; height: 100%; }
  .brand-name {
    font-family: "Fira Sans", sans-serif;
    font-weight: 700;
    fill: var(--swiss-red);
  }
  .variety {
    font-family: "Fira Sans", sans-serif;
    font-weight: 700;
    fill: var(--herb-green);
    letter-spacing: 2px;
  }
  .claim {
    font-family: "Fira Sans", sans-serif;
    font-weight: 400;
    fill: var(--text-light);
    letter-spacing: 2px;
  }
</style>
</head>
<body>
<main class="sheet">

  <!-- Lid label with alpine scene -->
  <div class="label label--scenic">
    <svg viewBox="0 0 400 400" aria-labelledby="scenic-title">
      <title id="scenic-title">Deckeletikett Pfeffling Kräutermischung mit Alpenlandschaft</title>
      <defs>
        <clipPath id="scenic-disc"><circle cx="200" cy="200" r="196"/></clipPath>
        <linearGradient id="scenic-sky" x1="0" y1="0" x2="0" y2="1">
          <stop offset="0" stop-color="#f3e27a"/>
          <stop offset="0.25" stop-color="var(--sky)"/>
          <stop offset="0.8" stop-color="#c9d9d8"/>
          <stop offset="1" stop-color="var(--meadow)"/>
        </linearGradient>
        <linearGradient id="scenic-red" x1="0" y1="0" x2="1" y2="0">
          <stop offset="0" stop-color="var(--swiss-red-deep)"/>
          <stop offset="0.5" stop-color="var(--swiss-red)"/>
          <stop offset="1" stop-color="var(--swiss-red-deep)"/>
        </linearGradient>
      </defs>
      <g clip-path="url(#scenic-disc)">
        <rect class="alpine-scene" x="0" y="0" width="400" height="263" fill="url(#scenic-sky)" role="img" aria-label="Illustration: Sonne über Alpenbergen mit See und Wiesenkräutern"/>
        <rect class="white-stripe" x="0" y="263" width="400" height="9" fill="var(--stripe-white)"/>
        <rect class="red-field" x="0" y="272" width="400" height="128" fill="url(#scenic-red)"/>
      </g>
      <circle class="rim" cx="200" cy="200" r="196" fill="none" stroke="var(--herb-green)" stroke-width="6"/>
      <text class="brand-name" x="200" y="128" text-anchor="middle" font-size="46">Pfeffling</text>
      <text class="variety" x="200" y="162" text-anchor="middle" font-size="13">Kräutermischung</text>
      <g class="swiss-flag">
        <rect x="171" y="237" width="58" height="58" fill="var(--stripe-white)" stroke="#cfcfcf" stroke-width="1"/>
        <rect x="177" y="243" width="46" height="46" fill="var(--swiss-red)"/>
        <rect x="195" y="252" width="10" height="28" fill="var(--text-light)"/>
        <rect x="186" y="261" width="28" height="10" fill="var(--text-light)"/>
      </g>
      <text class="claim" x="200" y="313" text-anchor="middle" font-size="9.5">Traditional Swiss Formula</text>
    </svg>
  </div>

  <!-- Lid label, plain variant -->
  <div class="label label--plain">
    <svg viewBox="0 0 400 400" aria-labelledby="plain-title">
      <title id="plain-title">Deckeletikett Pfeffling Kräutermischung, schlichte Variante</title>
      <defs>
        <clipPath id="plain-disc"><circle cx="200" cy="200" r="196"/></clipPath>
        <linearGradient id="plain-red" x1="0" y1="0" x2="1" y2="0">
          <stop offset="0" stop-color="var(--swiss-red-deep)"/>
          <stop offset="0.5" stop-color="var(--swiss-red)"/>
          <stop offset="1" stop-color="var(--swiss-red-deep)"/>
        </linearGradient>
      </defs>
      <g clip-path="url(#plain-disc)">
        <rect class="white-field" x="0" y="0" width="400" height="263" fill="var(--label-white)"/>
        <rect class="white-stripe" x="0" y="263" width="400" height="9" fill="var(--stripe-white)"/>
        <rect class="red-field" x="0" y="272" width="400" height="128" fill="url(#plain-red)"/>
      </g>
      <circle class="rim" cx="200" cy="200" r="196" fill="none" stroke="var(--herb-green)" stroke-width="6"/>
      <text class="brand-name" x="200" y="88" text-anchor="middle" font-size="34">Pfeffling</text>
      <text class="variety" x="200" y="114" text-anchor="middle" font-size="10">Kräutermischung</text>
      <g class="swiss-flag">
        <rect x="171" y="237" width="58" height="58" fill="var(--stripe-white)" stroke="#cfcfcf" stroke-width="1"/>
        <rect x="177" y="243" width="46" height="46" fill="var(--swiss-red)"/>
        <rect x="195" y="252" width="10" height="28" fill="var(--text-light)"/>
        <rect x="186" y="261" width="28" height="10" fill="var(--text-light)"/>
      </g>
      <text class="claim" x="200" y="313" text-anchor="middle" font-size="9.5">Traditional Swiss Formula</text>
    </svg>
  </div>

</main>
</body>
</html>
```